Swimming Pool Service Website needed!!!

Hi Everyone! Thanks for looking at my contest. I PROMISE to provide excellent feedback during this process.

I am starting a new swimming pool business cleaning company in San Diego, California and would like your help in making it similar to one of these two websites that are already functioning.

http://www.brightlagoonworks.example/services-repair.html

http://tidemarkaquacare.example/commercial-pool-cleaning.php

I like these two because they are easy to read, classy, sophisticated and have nice pictures of really clean & clear pools.

I really like the blue on white color format.

I do not have a logo, but the name of my company is GLIMMERWAVE POOL SERVICE.

My tag line is: Water so pure, it sparkles like a summer sky. (does not need to have the quotes around "in"...maybe just italics for this word IN?) You decide for me.

I would like to have a logo designed that incorporates some sort of easy to read letters. I do not want cursive (handwriting) letters. I thought about having a "reflection" of letters (mirror image), but think that this will be hard to read from far away. Maybe you can surprise me and come up with an idea that works using the a mirror image....but I'm not sure. I was leaning toward plain old BLOCK letters as I think it would be easy to read on my truck.

I would like to have 5 pages on my website:
1) Home
2) About Us (Know Your Poolman) / Why Hire Us
3) Services Offered
4) FAQ's
5) Contact

I am looking for a fully-functioning website (coded). Upon selection of the design winner, I am offering to increase the budget/payment by $100-$125 for the coding of all the pages. So anyone looking at participating in this contest, should be willing and able to provide the coding to the webpages that i've requested.

Target Market(s)

Upper middle-class homeowners who have a pool

Industry/Entity Type

Pool Service

Number of Pages Required

5+ page

Font styles to use
Serif

Colors
0455a3
3276b5
85acd3
85cae6
ffffff
33a6d7
0592cd

Requirements
Must have
• The Home page must have this picture highlighted in the top of the page:
• http://www.mesawaterpro.example/
• Must have pictures of some high-end pools. Any that you can find on the internet are wonderful.
• Must have a table on the right of the home page that mentions the service areas that we go to:
• • Carmel Valley (92130)
• • Del Mar (92014)
• • Rancho Santa Fe (92067)
• • Solana Beach (92075)
• • Santaluz (92127)
• • Cardiff (92007)
• • Encinitas (92024)
• • Carlsbad (92009, 92008)
• • La Jolla (92037)
• • Pacific Beach (92109)
• • Mira Mesa (92126)
• • Sorrento Valley (92121)
• • Clairemont (92117)
• • Rancho Bernardo (92127, 92128)
• • Rancho Penasquitos (92129)
• • Poway (92064)
• •
Nice to have
• Maybe incorporate some pictures of some kids (or families) playing in pools on the Why Hire Us page?
• I also like the feel of this website, but posting this page just for reference so you can get a feel more of what I like:
• http://www.crestlinepool.example/
• I like the FAQ's page from this website. I like how you can click on the question and then it pops up with the answer. http://www.dunewoodpoolcare.example/pool-spa-fountain-faqs/

```html
<!DOCTYPE html>
<html lang="en">
<head>
<meta charset="utf-8">
<title>GlimmerWave Pool Service</title>
<link href="https://fonts.googleapis.com/css2?family=Open+Sans:ital,wght@0,400;0,600;0,700;1,400;1,600&family=Oswald:wght@400;500&display=swap" rel="stylesheet">
<style>
:root{
  --navy:#0455a3;
  --blue:#3276b5;
  --sky:#85acd3;
  --aqua:#85cae6;
  --bright:#0592cd;
  --cyan:#33a6d7;
  --white:#ffffff;
  --ink:#333b45;
  --muted:#6a737d;
  --band:#dfe9f4;
  --line:#c9d3de;
}
*{margin:0;padding:0;box-sizing:border-box}
html,body{width:804px;height:1200px;overflow:hidden;background:var(--white)}
body{position:relative;font-family:"Open Sans",Arial,sans-serif;color:var(--ink)}
.abs{position:absolute}

/* header */
.brand{left:122px;top:78px;display:flex;align-items:center;gap:7px}
.brand-dot{width:18px;height:18px;border-radius:50%;background:var(--navy)}
.brand-name{font-family:"Oswald",sans-serif;font-weight:500;font-size:16px;color:var(--navy);line-height:1;letter-spacing:.4px}
.tagline{left:330px;top:80px;width:352px;text-align:right;font-style:italic;font-weight:600;font-size:11.5px;color:var(--bright)}
.nav{left:282px;top:104px;display:flex;font-size:10px;text-transform:uppercase}
.nav a{color:var(--blue);text-decoration:none;padding:3px 9px;border-right:1px solid var(--line)}
.nav a:last-child{border-right:none}
.nav a.active{color:var(--navy);border-bottom:2px solid var(--cyan)}

/* hero */
.hero{left:0;top:130px;width:804px;height:284px;background:linear-gradient(180deg,#7cc9ea 0%,#3fa9d9 45%,#1a86c2 100%)}
.hero-panel{left:262px;top:150px;width:300px;height:128px;background:rgba(255,255,255,.35)}
.hero-text{left:212px;top:158px;width:400px;text-align:center;color:var(--white);font-family:"Oswald",sans-serif;text-shadow:0 1px 2px rgba(0,0,0,.25)}
.hero-text .lead{font-size:21px;line-height:23px}
.hero-text .sub{font-size:15px;margin-top:2px}
.hero-text .call{font-size:19px;line-height:22px;margin-top:16px}
.hero-text .call b{font-weight:500}
.dots{left:384px;top:404px;display:flex;gap:5px}
.dots span{width:6px;height:6px;border-radius:50%;background:rgba(255,255,255,.6)}
.dots span.on{background:var(--white)}

/* features */
.feature{top:450px;width:146px;text-align:center}
.feature svg{display:block;margin:0 auto 8px}
.feature h3{font-size:9.5px;font-weight:600;color:var(--bright);margin-bottom:8px;white-space:nowrap}
.feature p{font-size:8.3px;line-height:12px;text-align:left;color:var(--ink)}

/* service areas */
.areas{left:112px;top:650px;width:322px;height:223px;border:1px solid var(--line);padding:10px 12px}
.box-title{display:flex;align-items:center;gap:8px;font-family:"Oswald",sans-serif;font-size:17px;font-weight:400;color:var(--ink)}
.areas p{font-size:7.6px;line-height:11px;margin:8px 0 6px}
.area-list{display:grid;grid-template-columns:1fr 1fr;column-gap:8px;list-style:none;font-size:7.8px;line-height:11.2px;padding-left:6px}
.area-list li::before{content:"•";color:var(--bright);margin-right:6px}

/* testimonials */
.reviews{left:445px;top:650px;width:256px;height:223px;background:#f3f4f6;padding:10px 12px}
.quote{font-size:7.4px;line-height:10px;font-style:italic;color:var(--muted);margin-top:8px}
.quote cite{display:block;text-align:right;font-style:normal;margin-top:2px;color:var(--ink)}

/* location band */
.band{left:0;top:885px;width:804px;height:252px;background:var(--band)}
.loc-title{left:112px;top:898px;font-family:"Oswald",sans-serif;font-size:17px;font-weight:400}
.map{left:112px;top:927px;width:195px;height:138px;background:linear-gradient(135deg,#e8eee4,#d6e3d1 60%,#e4e6df);border:1px solid var(--line)}
.contact{left:325px;top:898px;width:160px;font-size:9px;line-height:12px}
.contact dt{font-weight:700;font-size:8.5px;margin-top:9px}
.contact dt:first-child{margin-top:0}
.badges{left:335px;top:1060px;display:flex;gap:10px}
.badges span{width:50px;height:50px;border-radius:50%;background:var(--navy);border:3px solid var(--sky)}
.card{left:492px;top:889px;width:208px;height:232px;background:var(--white);padding:8px;text-align:center}
.card-photo{width:192px;height:124px;background:linear-gradient(180deg,#4fc0ea,#1a8fcf)}
.card p{font-size:8.5px;line-height:11.5px;margin-top:8px;color:var(--ink)}
.card .phone{font-family:"Oswald",sans-serif;font-size:17px;color:var(--bright);margin-top:8px}

/* footer */
.footer{left:112px;top:1150px;width:590px;font-size:7.5px;color:var(--muted)}
</style>
</head>
<body>

<div class="abs brand"><span class="brand-dot"></span><span class="brand-name">GLIMMERWAVE POOL SERVICE</span></div>
<div class="abs tagline">“Water so pure, it sparkles like a summer sky.”</div>
<nav class="abs nav">
  <a class="active" href="#">Home</a><a href="#">About Us</a><a href="#">Services Offered</a><a href="#">FAQs</a><a href="#">Why Hire Us</a><a href="#">Contact</a>
</nav>

<div class="abs hero" role="img" aria-label="Family smiling together at the edge of a bright blue swimming pool"></div>
<div class="abs hero-panel"></div>
<div class="abs hero-text">
  <div class="lead">Leading San Diego swimming pool<br>and spa service company</div>
  <div class="sub">Both commercial and residential</div>
  <div class="call">Call us now to schedule a FREE<br>pool and needs assessment <b>(858) 555-0192</b></div>
</div>
<div class="abs dots"><span class="on"></span><span></span><span></span><span></span></div>

<section class="abs feature" style="left:98px">
  <svg width="40" height="40" viewBox="0 0 40 40"><circle cx="20" cy="20" r="15" fill="none" stroke="var(--bright)" stroke-width="7"/><circle cx="20" cy="20" r="15" fill="none" stroke="var(--white)" stroke-width="7" stroke-dasharray="6 17.5"/><circle cx="20" cy="20" r="18.5" fill="none" stroke="var(--bright)" stroke-width="1"/></svg>
  <h3>We are certified.</h3>
  <p>We are certified by the Aquatic Care Standards Council as Certified Water Care Technicians (CWT).</p>
</section>
<section class="abs feature" style="left:256px">
  <svg width="40" height="40" viewBox="0 0 40 40"><path d="M10 21l7 7 14-15" fill="none" stroke="var(--bright)" stroke-width="4"/><path d="M4 34q4-3 8 0t8 0 8 0 8 0" fill="none" stroke="var(--bright)" stroke-width="2"/></svg>
  <h3>We are a reliable service.</h3>
  <p>Your pool – and your business – is very important to us. Count on Ripplecrest Pool Co. to show up week in and week out (in uniform), return phone calls, and provide consistent top-notch service.</p>
</section>
<section class="abs feature" style="left:414px">
  <svg width="40" height="40" viewBox="0 0 40 40"><path d="M4 20q4-4 8 0t8 0 8 0 8 0M4 27q4-4 8 0t8 0 8 0 8 0M4 34q4-4 8 0t8 0 8 0 8 0" fill="none" stroke="var(--bright)" stroke-width="2.6"/><circle cx="28" cy="10" r="4" fill="var(--bright)"/></svg>
  <h3>We are bonded and insured.</h3>
  <p>We are bonded and also have a $3,000,000 insurance policy to provide you with peace of mind.</p>
</section>
<section class="abs feature" style="left:572px">
  <svg width="40" height="40" viewBox="0 0 40 40"><path d="M7 18L20 7l13 11" fill="none" stroke="var(--bright)" stroke-width="3"/><rect x="11" y="18" width="18" height="9" fill="var(--bright)"/><path d="M4 33q4-3 8 0t8 0 8 0 8 0" fill="none" stroke="var(--bright)" stroke-width="2.4"/></svg>
  <h3>We promise. No surprises.</h3>
  <p>We respect your privacy and your property. We won’t enter your backyard unannounced on an unexpected day. We won’t drop an appointment without notifying you in advance. And we won’t leave your home or your property in any different condition than you would yourself.</p>
</section>

<section class="abs areas">
  <h2 class="box-title"><svg width="20" height="20" viewBox="0 0 20 20"><circle cx="10" cy="10" r="7.5" fill="none" stroke="var(--bright)" stroke-width="3"/><circle cx="10" cy="10" r="2" fill="var(--bright)"/></svg>Service Areas</h2>
  <p>GlimmerWave Pool Service provides full range of service and maintenance for commercial and residential pools, spas, waterfalls and fountains. We are proud to provide our honest and highly professional services for following San Diego county areas:</p>
  <ul class="area-list">
    <li>Carmel Valley (92130)</li><li>La Jolla (92037)</li>
    <li>Del Mar (92014)</li><li>Pacific Beach (92109)</li>
    <li>Rancho Santa Fe (92067)</li><li>Mira Mesa (92126)</li>
    <li>Solana Beach (92075)</li><li>Sorrento Valley (92121)</li>
    <li>Santaluz (92127)</li><li>Clairemont (92117)</li>
    <li>Cardiff (92007)</li><li>Rancho Bernardo (92127, 92128)</li>
    <li>Encinitas (92024)</li><li>Rancho Penasquitos (92129)</li>
    <li>Carlsbad (92009, 92008)</li><li>Poway (92064)</li>
  </ul>
</section>

<section class="abs reviews">
  <h2 class="box-title"><svg width="20" height="18" viewBox="0 0 20 18"><path d="M2 2h16v10H8l-4 4v-4H2z" fill="none" stroke="var(--bright)" stroke-width="2"/></svg>People say the nicest things</h2>
  <blockquote class="quote">“Working with Marco is terrific. His education and professional background sets him apart from all the other pool cleaners. He has excellent communication with us and he shows up when he says he will. GlimmerWave is the only pool company I have ever recommended to my friends.”<cite>– Dale Whitford</cite></blockquote>
  <blockquote class="quote">“GlimmerWave is so honest as they come. I am very happy with their service and know-how, and my pool has never looked better.”<cite>– Lena Castillo</cite></blockquote>
  <blockquote class="quote">“The service is awesome! No shortcuts are taken to save time. The monthly cost of Marco’s great quality work is the best value in town. I highly recommend that you give Marco and GlimmerWave a try. Keep up the great work!”<cite>– Rosa Lindqvist</cite></blockquote>
</section>

<div class="abs band"></div>
<h2 class="abs loc-title">Our Location</h2>
<div class="abs map" role="img" aria-label="Street map of the San Diego area marking the office location"></div>
<dl class="abs contact">
  <dt>ADDRESS:</dt><dd>1840 Harborlight Way #210<br>San Diego, CA 92130</dd>
  <dt>PHONE:</dt><dd>(858) 555-0192</dd>
  <dt>EMAIL:</dt><dd>hello@glimmerwavepools.example</dd>
  <dt>WEBSITE:</dt><dd>www.glimmerwavepools.example</dd>
</dl>
<div class="abs badges"><span></span><span></span></div>
<aside class="abs card">
  <div class="card-photo" role="img" aria-label="Child swimming underwater in a clear blue pool"></div>
  <p>GlimmerWave Pool Service is a leading San Diego swimming pool &amp; spa service company for both residential and commercial pools.</p>
  <div class="phone">CALL US (858) 555-0192</div>
</aside>

<footer class="abs footer">Copyright ©2015 by GlimmerWave Pool Service • All Rights Reserved • Contact Webmaster</footer>

</body>
</html>
```